Design and code ShopVantel website

Website is currently up and running but looking for a fresh and new theme or design for it.

Must interact perfectly with ShopVantel

Will provide plenty of images.

All content should stay exactly the same as far as text and information.

Looking for a dark but elegant theme. All of the information necessary is listed.

Will need detailed instructions on how to implement the website into our current system... simply looking to make our page unique and not just a stock ShopVantel theme

Coding

Coded - Design and coding required

Number of Pages Required

5+ page

Colors
000000
9d9d9d
ffffff

Requirements
Must have
• same information as www.morvellinavapors.example

```html
<!DOCTYPE html>
<html lang="en">
<head>
<meta charset="utf-8">
<title>Morvellina Vapors</title>
<link href="https://fonts.googleapis.com/css2?family=Roboto:wght@400;500;700&display=swap" rel="stylesheet">
<style>
:root{
  --black:#000000;
  --ink:#1e1e1e;
  --grey:#9d9d9d;
  --text:#555555;
  --line:#d6d6d6;
  --white:#ffffff;
  --accent:#d94444;
  --footer:#2f2f33;
  --footer-bottom:#232326;
  --photo-dark:#141414;
}
*{box-sizing:border-box;margin:0;padding:0}
html,body{width:1200px;height:2571px;overflow:hidden}
body{position:relative;background:var(--white);font-family:'Roboto',Arial,sans-serif;color:var(--ink)}
.abs{position:absolute}
a{color:inherit;text-decoration:none}

/* top bar */
.topbar{left:0;top:0;width:1200px;height:38px;background:var(--black);color:var(--white);font-size:11px;font-weight:500}
.topbar .item{position:absolute;top:0;height:38px;display:flex;align-items:center;gap:7px}
.topbar .divider{position:absolute;top:9px;width:1px;height:20px;background:#444}

/* sidebar */
.brand{left:99px;top:108px;width:235px;font-size:27px;font-weight:700;color:var(--ink);letter-spacing:.5px;line-height:1.1}
.search{left:99px;top:211px;width:234px;height:41px;border:1px solid var(--line);display:flex;align-items:center;justify-content:space-between;padding:0 14px;font-size:13px;color:#777}
.nav{left:99px;top:284px;list-style:none}
.nav li{height:40.4px;display:flex;align-items:flex-start;font-size:11.5px;color:#666;letter-spacing:.3px}
.nav li::before{content:"";width:0;height:0;border-left:5px solid #aaa;border-top:4px solid transparent;border-bottom:4px solid transparent;margin:2px 12px 0 2px}
.nav li.active{color:var(--accent)}
.nav li.active::before{border-left-color:var(--accent)}

/* hero */
.hero{left:370px;top:77px;width:732px;height:485px;background:var(--black)}
.hero-photo{position:absolute;left:0;top:0;width:732px;height:485px;background:radial-gradient(ellipse at 80% 45%,#6a5a36 0%,#2a2416 30%,transparent 55%),linear-gradient(180deg,#000 0%,#000 55%,#3a2c1c 80%,#1a140c 100%)}
.hero-brand{left:84px;top:60px;font-size:30px;font-weight:700;color:var(--white)}
.hero-copy{left:84px;top:155px;width:250px;font-size:10.5px;line-height:24px;color:var(--white);font-weight:500;letter-spacing:.3px}
.hero-btn{left:84px;top:245px;width:158px;height:45px;background:var(--accent);color:var(--white);font-size:14px;display:flex;align-items:center;justify-content:center;gap:6px}

/* sections */
.section-title{left:370px;width:732px;text-align:center;font-size:22px;font-weight:700;color:var(--ink);letter-spacing:.3px}
.card{position:absolute;width:225px}
.card .photo{width:225px;height:206px;background:radial-gradient(ellipse at 50% 60%,#4a3e28 0%,#201a10 35%,var(--photo-dark) 70%)}
.card .name{margin-top:27px;text-align:center;font-size:15px;color:var(--ink);letter-spacing:.3px}
.card .row{margin-top:18px;display:flex;align-items:center;justify-content:space-between;padding-left:9px;padding-right:9px}
.card .price{font-size:20px;color:var(--accent)}
.card .buy{width:106px;height:31px;border:1px solid var(--accent);color:var(--accent);font-size:11px;display:flex;align-items:center;justify-content:center}

.post{position:absolute;width:225px}
.post .photo{width:225px;height:192px}
.post h3{margin-top:21px;font-size:12.5px;font-weight:500;line-height:24px;color:var(--ink)}
.post .date{margin-top:10px;font-size:10px;color:#666;display:flex;align-items:center;gap:8px}
.post p{margin-top:16px;font-size:10.5px;line-height:20px;color:#666}

.newsletter-title{left:370px;top:2071px;width:732px;text-align:center;font-size:21px;color:var(--ink)}
.email{left:465px;top:2127px;width:380px;height:40px;border:1px solid var(--line);font-size:12px;color:#aaa;display:flex;align-items:center;padding-left:17px}
.subscribe{left:857px;top:2127px;width:151px;height:40px;background:var(--accent);color:var(--white);font-size:14px;display:flex;align-items:center;justify-content:center}

/* footer */
.footer{left:0;top:2247px;width:1200px;height:273px;background:var(--footer);color:#cfcfcf}
.fcol{position:absolute;top:48px}
.fcol h4{font-size:15px;font-weight:400;color:var(--white);margin-bottom:17px;letter-spacing:.3px}
.fcol li{list-style:none;font-size:11px;height:25px}
.contact .name{color:var(--accent);font-size:12px;margin-bottom:12px}
.contact p{font-size:11px;line-height:22px}
.contact .phone{display:flex;align-items:center;gap:8px;margin-top:8px}
.social{display:flex;gap:9px;margin-top:18px}
.social span{width:20px;height:20px;border-radius:50%;background:#6d6d70}
.footer-brand{left:895px;top:110px;width:210px;font-size:26px;font-weight:700;color:var(--white)}
.bottombar{left:0;top:2520px;width:1200px;height:51px;background:var(--footer-bottom);color:#bbb;font-size:11px;display:flex;align-items:center;justify-content:center}
</style>
</head>
<body>

<header class="abs topbar">
  <div class="item" style="left:99px">
    <svg width="14" height="14" viewBox="0 0 14 14" fill="none" stroke="#fff" stroke-width="1.3"><circle cx="7" cy="4.5" r="3"/><path d="M1.5 13.5c0-3 2.5-5 5.5-5s5.5 2 5.5 5"/></svg>
    ACCOUNT
    <svg width="8" height="5" viewBox="0 0 8 5" fill="none" stroke="#fff" stroke-width="1.2"><path d="M1 1l3 3 3-3"/></svg>
  </div>
  <div class="divider" style="left:222px"></div>
  <div class="item" style="left:252px">USD
    <svg width="13" height="9" viewBox="0 0 13 9"><rect width="13" height="9" fill="#c33"/><rect y="2" width="13" height="1.5" fill="#fff"/><rect y="5" width="13" height="1.5" fill="#fff"/><rect width="6" height="4.5" fill="#339"/></svg>
    <svg width="8" height="5" viewBox="0 0 8 5" fill="none" stroke="#fff" stroke-width="1.2"><path d="M1 1l3 3 3-3"/></svg>
  </div>
  <div class="item" style="left:992px">
    <svg width="16" height="14" viewBox="0 0 16 14" fill="none" stroke="#fff" stroke-width="1.4"><path d="M8 13S1 8.5 1 4.5A3.3 3.3 0 0 1 8 3a3.3 3.3 0 0 1 7 1.5C15 8.5 8 13 8 13z"/></svg>
  </div>
  <div class="divider" style="left:1029px"></div>
  <div class="item" style="left:1047px">$0.00
    <svg width="14" height="15" viewBox="0 0 14 15" fill="none" stroke="#fff" stroke-width="1.4" style="margin-left:6px"><rect x="1" y="4" width="12" height="10"/><path d="M4.5 6V3a2.5 2.5 0 0 1 5 0v3"/></svg>
  </div>
</header>

<aside>
  <div class="abs brand">Morvellina Vapors</div>
  <div class="abs search">Search
    <svg width="14" height="14" viewBox="0 0 14 14" fill="none" stroke="#aaa" stroke-width="1.3"><circle cx="6" cy="6" r="4.5"/><path d="M9.5 9.5L13 13"/></svg>
  </div>
  <ul class="abs nav">
    <li class="active">HOME</li>
    <li>ABOUT US</li>
    <li>WHOLESALE</li>
    <li>WHY CHOOSE US?</li>
    <li>CPSC INFO</li>
    <li>SHIPPING &amp; RETURNS</li>
    <li>CONTACT</li>
  </ul>
</aside>

<section class="abs hero">
  <div class="hero-photo" role="img" aria-label="Dropper bottles of e-liquid beside pistachio pastries on a black background"></div>
  <div class="abs hero-brand">Morvellina Vapors</div>
  <p class="abs hero-copy">MORVELLINA VAPORS IS FOUNDED BY ELIAS CORWIN WHO IS A SIX YEAR MEMBER OF THE ELECTRONIC CIGARETTE INDUSTRY.</p>
  <a class="abs hero-btn">SHOP ONLINE
    <svg width="10" height="9" viewBox="0 0 10 9" fill="none" stroke="#fff" stroke-width="1.4"><path d="M1 1l3.5 3.5L1 8M5 1l3.5 3.5L5 8"/></svg>
  </a>
</section>

<h2 class="abs section-title" style="top:633px">NEW ARRIVALS</h2>
<div class="card" style="left:370px;top:703px">
  <div class="photo" role="img" aria-label="E-liquid bottle with cream pastries"></div>
  <div class="name">E-LIQUID</div>
  <div class="row"><span class="price">$19.99</span><a class="buy">BUY NOW</a></div>
</div>
<div class="card" style="left:624px;top:703px">
  <div class="photo" role="img" aria-label="Torta Be True bottle with pistachio pastries"></div>
  <div class="name">TORTA BE TRUE</div>
  <div class="row"><span class="price">$19.99</span><a class="buy">BUY NOW</a></div>
</div>
<div class="card" style="left:878px;top:703px">
  <div class="photo" role="img" aria-label="Three e-liquid bottles with pistachios"></div>
  <div class="name">MERCHANDISE</div>
  <div class="row"><span class="price">$19.99</span><a class="buy">BUY NOW</a></div>
</div>

<h2 class="abs section-title" style="top:1096px">FEATURED PRODUCTS</h2>
<div class="card" style="left:370px;top:1166px">
  <div class="photo" role="img" aria-label="E-liquid bottle with a strawberry pastry"></div>
  <div class="name">E-LIQUID</div>
  <div class="row"><span class="price">$19.99</span><a class="buy">BUY NOW</a></div>
</div>
<div class="card" style="left:624px;top:1166px">
  <div class="photo" role="img" aria-label="Torta Be True bottle with pistachio pastries"></div>
  <div class="name">TORTA BE TRUE</div>
  <div class="row"><span class="price">$19.99</span><a class="buy">BUY NOW</a></div>
</div>
<div class="card" style="left:878px;top:1166px">
  <div class="photo" role="img" aria-label="E-liquid bottle with cream pastries"></div>
  <div class="name">MERCHANDISE</div>
  <div class="row"><span class="price">$19.99</span><a class="buy">BUY NOW</a></div>
</div>

<h2 class="abs section-title" style="top:1540px">FROM OUR BLOG</h2>
<article class="post" style="left:370px;top:1608px">
  <div class="photo" role="img" aria-label="Person exhaling vapor indoors" style="background:linear-gradient(135deg,#6a5a58,#2a2224 60%,#8a7a72)"></div>
  <h3>CONTRIBUTED TO NUMEROUS ADVOCACY AND ACTIVIST</h3>
  <div class="date"><svg width="11" height="11" viewBox="0 0 11 11" fill="none" stroke="#888"><rect x=".5" y="1.5" width="10" height="9"/><path d="M.5 4h10M3 0v3M8 0v3"/></svg>7th Jan 2016</div>
  <p>Lorem ipsum dolor sit amet, consectetur adipiscing elit. Praesent ultrices metus in orci eleifend lobortis. Mauris semper ac lorem sed consequat...</p>
</article>
<article class="post" style="left:624px;top:1608px">
  <div class="photo" role="img" aria-label="Illustrated pastries on a dark chalkboard" style="background:radial-gradient(ellipse at 50% 55%,#7a5a2a,#2c3030 60%)"></div>
  <h3>CONTRIBUTED TO NUMEROUS ADVOCACY AND ACTIVIST</h3>
  <div class="date"><svg width="11" height="11" viewBox="0 0 11 11" fill="none" stroke="#888"><rect x=".5" y="1.5" width="10" height="9"/><path d="M.5 4h10M3 0v3M8 0v3"/></svg>7th Jan 2016</div>
  <p>Lorem ipsum dolor sit amet, consectetur adipiscing elit. Praesent ultrices metus in orci eleifend lobortis. Mauris semper ac lorem sed consequat...</p>
</article>
<article class="post" style="left:878px;top:1608px">
  <div class="photo" role="img" aria-label="Person sitting in a sunlit field at sunset" style="background:linear-gradient(180deg,#e9b060 0%,#c88a3a 45%,#6a7a2a 70%,#4a5a1e 100%)"></div>
  <h3>CONTRIBUTED TO NUMEROUS ADVOCACY AND ACTIVIST</h3>
  <div class="date"><svg width="11" height="11" viewBox="0 0 11 11" fill="none" stroke="#888"><rect x=".5" y="1.5" width="10" height="9"/><path d="M.5 4h10M3 0v3M8 0v3"/></svg>7th Jan 2016</div>
  <p>Lorem ipsum dolor sit amet, consectetur adipiscing elit. Praesent ultrices metus in orci eleifend lobortis. Mauris semper ac lorem sed consequat...</p>
</article>

<h2 class="abs newsletter-title">SUBSCRIBE TO OUR NEWSLETTER</h2>
<div class="abs email">Enter your email id</div>
<a class="abs subscribe">SUBSCRIBE</a>

<footer class="abs footer">
  <div class="fcol" style="left:99px">
    <h4>WELCOME</h4>
    <ul><li>Wholesale</li><li>Why Choose Us?</li><li>CPSC Info</li><li>Terms &amp; Conditions</li><li>Shipping &amp; Returns</li><li>Contact</li></ul>
  </div>
  <div class="fcol" style="left:300px">
    <h4>MY ACCOUNT</h4>
    <ul><li>My Account</li><li>My Cart</li><li>Login</li><li>Register</li></ul>
  </div>
  <div class="fcol" style="left:487px">
    <h4>INFORMATION</h4>
    <ul><li>Privacy Policy</li><li>Terms &amp; Conditions</li><li>Disclaimer</li><li>Sitemap</li></ul>
  </div>
  <div class="fcol contact" style="left:691px">
    <h4>CONTACT US</h4>
    <div class="name">Morvellina Vapors</div>
    <p>18 Alder Lane, STE 4<br>Brookfield, MA 02190</p>
    <p class="phone"><svg width="10" height="10" viewBox="0 0 10 10"><path d="M2 0l2 2.5-1 1.2a6 6 0 0 0 3.3 3.3l1.2-1L10 8l-1.5 2C4 10 0 6 0 1.5z" fill="#cfcfcf"/></svg>Phone: 555-201-4471</p>
    <div class="social"><span></span><span></span><span></span><span></span><span></span></div>
  </div>
  <div class="abs footer-brand">Morvellina Vapors</div>
</footer>
<div class="abs bottombar">© 2016. Morvellina Vapors. All rights reserved.</div>

</body>
</html>
```